Business Card Design

Electronic Security
Alarm Systems
CCTV
Electronic Access Control
Security System Integration

Industry/Entity Type

Business

Contact Information for Business Card

Gareth Linwood
PO Box 862
Yarrowdale Qld 4173
Phone 07 38265140
Mob 0428637291

```html
<!DOCTYPE html>
<html lang="en">
<head>
<meta charset="utf-8">
<title>Tarrant Security — Business Card</title>
<link rel="stylesheet" href="https://fonts.googleapis.com/css2?family=Open+Sans:wght@400;600;700&display=swap">
<style>
  :root {
    --paper: #ffffff;
    --ink: #111111;
    --slate: #4f6f82;
    --label-blue: #3a93c2;
    --band-warm: #b7561f;
    --band-mid: #5a2e2a;
    --band-dark: #0d1419;
    --band-text: #ffffff;
  }
  * { margin: 0; padding: 0; box-sizing: border-box; }
  html, body {
    width: 1200px;
    height: 741px;
    overflow: hidden;
    background: var(--paper);
  }
  .card {
    position: relative;
    width: 1200px;
    height: 741px;
    background: var(--paper);
    font-family: "Open Sans", Arial, sans-serif;
    color: var(--ink);
  }
  .brand {
    position: absolute;
    left: 60px;
    top: 300px;
    width: 480px;
    display: flex;
    align-items: center;
    justify-content: center;
    gap: 22px;
  }
  .brand-square {
    width: 46px;
    height: 46px;
    background: var(--slate);
  }
  .brand-name {
    font-size: 60px;
    font-weight: 600;
    color: var(--slate);
    letter-spacing: 1px;
  }
  .divider {
    position: absolute;
    left: 597px;
    top: 121px;
    width: 3px;
    height: 479px;
    background: var(--ink);
  }
  .contact {
    position: absolute;
    left: 657px;
    top: 160px;
  }
  .contact-name {
    font-size: 52px;
    font-weight: 700;
    color: var(--slate);
    text-transform: uppercase;
    letter-spacing: 0.5px;
    line-height: 1;
    margin-bottom: 34px;
  }
  .detail {
    display: grid;
    grid-template-columns: 170px auto;
    font-size: 28px;
    line-height: 37px;
    text-transform: uppercase;
    margin-bottom: 32px;
  }
  .detail-label {
    font-weight: 700;
    color: var(--label-blue);
  }
  .detail-value {
    font-weight: 400;
    color: var(--ink);
  }
  .services-band {
    position: absolute;
    left: 0;
    top: 636px;
    width: 1200px;
    height: 105px;
    background: linear-gradient(90deg, var(--band-warm) 0%, var(--band-mid) 35%, #1c2228 65%, var(--band-dark) 100%);
    display: flex;
    align-items: flex-start;
    justify-content: center;
    padding-top: 17px;
  }
  .services {
    font-size: 22.5px;
    font-weight: 700;
    color: var(--band-text);
    letter-spacing: 0.2px;
    white-space: nowrap;
  }
</style>
</head>
<body>
  <div class="card">
    <div class="brand">
      <span class="brand-square"></span>
      <span class="brand-name">TARRANT</span>
    </div>

    <div class="divider"></div>

    <div class="contact">
      <h1 class="contact-name">Gareth Linwood</h1>
      <div class="detail">
        <span class="detail-label">Address</span>
        <span class="detail-value">PO Box 862<br>Yarrowdale Qld<br>4173</span>
      </div>
      <div class="detail">
        <span class="detail-label">Phone</span>
        <span class="detail-value">07 38265140</span>
      </div>
      <div class="detail">
        <span class="detail-label">Mob</span>
        <span class="detail-value">0428637291</span>
      </div>
    </div>

    <div class="services-band">
      <p class="services">ALARM SYSTEMS • CCTV • ELECTRONIC ACCESS CONTROL • SECURITY SYSTEM INTEGRATION</p>
    </div>
  </div>
</body>
</html>
```